Fahrzeugbeschriftung Hörgeräteakustik
Ich war wirklich sehr zufrieden! Danke, dass Sie auf alle Wünsche so schnell eingegangen sind :)
Zielgruppe
Hörgeräteakustik // mobile Hörsystemversorgung
Leistungen: kostenloser Hörtest - Hörgeräteversorgung - Hausbesuch-Service - Flexible Terminabsprache
Aufgabenstellung
Wichtige Angaben:
Tilde-Marbach-Weg 7c, 59388 Soest
www.hoerakustik-lorenzen-beispiel.de
Fahrzeugdaten siehe Bilder: Veltra Caravo Mobil in Blazer Blue L1H1
Design kann auch gerne etwas witzig sein, sodass es Aufmerksamkeit erregt. Vielleicht ein Spruch auf der Heckklappe o.ä.

```html
<!DOCTYPE html>
<html lang="de">
<head>
<meta charset="utf-8">
<title>Fahrzeugbeschriftung Hörakustik Lorenzen</title>
<link rel="stylesheet" href="https://fonts.googleapis.com/css2?family=Marcellus+SC&family=Open+Sans:ital,wght@1,400&display=swap">
<style>
  :root {
    --van-blue: #1f3178;
    --band-green: #d3e6c6;
    --text-white: #ffffff;
    --service-cream: #f4f0d8;
  }
  html, body {
    margin: 0;
    padding: 0;
    overflow: hidden;
  }
  .livery {
    position: relative;
    width: 1200px;
    height: 703px;
    background: var(--van-blue);
    overflow: hidden;
    color: var(--text-white);
  }
  .livery__bands {
    position: absolute;
    inset: 0;
  }
  .brand {
    position: absolute;
    left: 222px;
    top: 176px;
    font-family: "Marcellus SC", serif;
    color: var(--text-white);
    line-height: 1.05;
    display: flex;
    align-items: center;
    gap: 10px;
  }
  .brand__dot {
    width: 12px;
    height: 12px;
    border-radius: 50%;
    background: var(--text-white);
  }
  .brand__name {
    font-size: 19px;
    letter-spacing: 0.5px;
  }
  .services {
    position: absolute;
    left: 413px;
    top: 168px;
    margin: 0;
    padding: 0;
    list-style: none;
    font-family: "Open Sans", sans-serif;
    font-style: italic;
    font-size: 16px;
    line-height: 19.5px;
    color: var(--service-cream);
  }
  .contact {
    position: absolute;
    left: 421px;
    top: 304px;
    font-family: "Marcellus SC", serif;
    color: var(--text-white);
  }
  .contact__address {
    font-size: 15px;
    line-height: 18px;
    letter-spacing: 0.3px;
  }
  .contact__phone {
    font-size: 36px;
    line-height: 42px;
    letter-spacing: 1px;
  }
  .contact__web {
    font-size: 15px;
    line-height: 16px;
    letter-spacing: 0.3px;
  }
</style>
</head>
<body>
  <main class="livery">
    <svg class="livery__bands" width="1200" height="703" viewBox="0 0 1200 703" aria-hidden="true">
      <polygon class="band band--upper" fill="var(--band-green)" points="239,240 850,274 910,326 239,245"/>
      <polygon class="band band--lower" fill="var(--band-green)" points="417,384 687,397 730,416 429,410"/>
    </svg>

    <div class="brand">
      <span class="brand__dot"></span>
      <span class="brand__name">Helene Lorenzen<br>Hörakustik</span>
    </div>

    <ul class="services">
      <li>free hearing test</li>
      <li>hearing aid supply</li>
      <li>home visit service</li>
      <li>flexible appointments</li>
    </ul>

    <div class="contact">
      <div class="contact__address">Tilde-Marbach-Weg 7c, 59388 Soest</div>
      <div class="contact__phone">02921 5550147</div>
      <div class="contact__web">www.hoerakustik-lorenzen-beispiel.de</div>
    </div>
  </main>
</body>
</html>
```